Pelbrook Metal Roofing INC.

Hello,
I am working with a local business to design them a new website. The designer I had worked with moved to colorado and has taken a new job. He recommended that I try posting my new jobs on here. I would need a design and assistance setting the site up on my host nimbus server. I work by myself and handle the sales side of things and need a designer that can help me out.
This company is a metal roofing business. The current page I made for them is www.pelbrookmetalinc.example

They would like the new site to be similar to http://www.tamblecreekalloy.example

Please let me know if this is something that you could do for us.
Updates

the company wants the site to look very similar to this http://www.tamblecreekalloy.exampleis that something you could do, please get in touch with me.Thanks Added Tuesday, January 10, 2017

Industry/Entity Type

Business

Font styles to use
Sans Serif

Colors
ed252d

Requirements
Must have
• the company wants the site to look very similar to this
• http://www.tamblecreekalloy.example
• is that something you could do, please get in touch with me.
• Thanks

```html
<!DOCTYPE html>
<html lang="en">
<head>
<meta charset="utf-8">
<title>Pelbrook Metal Inc</title>
<link rel="stylesheet" href="https://fonts.googleapis.com/css2?family=Roboto:wght@400;500;700&family=Open+Sans:wght@400&display=swap">
<style>
:root{
  --red:#ed252d;
  --red-dark:#c11218;
  --admin:#23282d;
  --gray-bg:#eeeeee;
  --tab-bg:#f2f2f2;
  --text:#333333;
  --nav:#555555;
  --white:#ffffff;
}
*{box-sizing:border-box;margin:0;padding:0}
html,body{width:1200px;height:1111px;overflow:hidden}
body{font-family:"Roboto",Arial,sans-serif;background:var(--white);position:relative;color:var(--text)}
.admin-bar{position:absolute;left:0;top:0;width:1200px;height:28px;background:var(--admin);color:#eee;font:13px "Open Sans",Arial,sans-serif;display:flex;align-items:center;padding:0 12px}
.admin-bar span{margin-right:18px;display:flex;align-items:center;gap:6px}
.admin-bar .right{margin-left:auto;margin-right:0}
.admin-bar .avatar{width:14px;height:14px;background:#ccc;display:inline-block}
.top-bar{position:absolute;left:0;top:28px;width:1200px;height:32px;background:var(--red);color:var(--white);font-size:11.5px;font-weight:700;display:flex;align-items:center;padding-left:134px;gap:16px}
.top-bar span{display:flex;align-items:center;gap:4px}
.site-header{position:absolute;left:0;top:60px;width:1200px;height:62px;background:var(--white);border-bottom:1px solid #e2e2e2}
.brand{position:absolute;left:136px;top:15px;width:138px;height:31px;border:2px solid #222;font-size:11px;letter-spacing:.3px;color:#333;display:flex;align-items:center;justify-content:center}
.main-nav{position:absolute;left:389px;top:29px;display:flex;gap:49px;font-size:13px;font-weight:500;color:var(--nav)}
.main-nav .active{color:var(--red)}
.content{position:absolute;left:0;top:122px;width:1200px;height:576px;background:var(--gray-bg)}
.slider-image{position:absolute;left:156px;top:72px;width:697px;height:432px;background:linear-gradient(135deg,#3a2a28 0%,#6b6f78 40%,#1f3f8a 55%,#8a8f99 75%,#b8b8b8 100%)}
.slider-tabs{position:absolute;left:853px;top:72px;width:202px;height:432px}
.tab{height:108px;padding:26px 0 0 18px;font-size:12px;line-height:23px;color:var(--text);border-bottom:1px solid #fff}
.tab:first-child{background:var(--tab-bg);position:relative}
.tab:first-child::before{content:"";position:absolute;left:-8px;top:44px;border:8px solid transparent;border-left:0;border-right-color:var(--tab-bg)}
.tab h3{font-size:12.5px;font-weight:500;line-height:18px;margin-bottom:0}
.site-footer{position:absolute;left:0;top:698px;width:1200px;height:362px;background:var(--red);color:var(--white)}
.col{position:absolute;top:62px;width:220px}
.col h2{font-size:16.5px;font-weight:400;margin-bottom:20px}
.service{display:flex;align-items:center;gap:9px;margin-bottom:4px}
.service .thumb{width:60px;height:60px;border-radius:50%;border:3px solid #fff;flex:none;background:linear-gradient(160deg,#8a5a3a,#c9b79a)}
.service p{font-size:11px;font-weight:500;line-height:24px;text-transform:uppercase}
.links li{list-style:none;font-size:12px;line-height:29px;display:flex;align-items:center;gap:8px}
.links li::before{content:"";width:5px;height:5px;border-radius:50%;background:#fff}
.hours p{font-size:12px;line-height:23px}
.hours b{font-weight:700}
.contact p{font-size:12px;line-height:23px}
.copyright{position:absolute;left:0;top:1060px;width:1200px;height:51px;background:var(--red-dark);color:var(--white);font-size:11.5px;display:flex;align-items:center;justify-content:center}
</style>
</head>
<body>
<div class="admin-bar">
  <span>My Blog</span><span>0</span><span>+ New</span><span>Edit Page</span><span>Enable Visual Builder</span>
  <span class="right">Howdy, admin <i class="avatar"></i>
    <svg width="13" height="13" viewBox="0 0 13 13"><circle cx="5" cy="5" r="4" fill="none" stroke="#ccc" stroke-width="2"/><path d="M8 8l4 4" stroke="#ccc" stroke-width="2"/></svg>
  </span>
</div>

<div class="top-bar">
  <span><svg width="9" height="9" viewBox="0 0 10 10"><path d="M2 0l2 2-1 2 3 3 2-1 2 2-2 2C4 10 0 6 0 2z" fill="#fff"/></svg>555-014-0765 FAX: 555-014-4931</span>
  <span><svg width="10" height="8" viewBox="0 0 10 8"><rect width="10" height="8" fill="#fff"/><path d="M0 0l5 4 5-4" stroke="#ed252d" fill="none"/></svg>support@pelbrook-metal-inc.example</span>
</div>

<header class="site-header">
  <div class="brand">PELBROOK METAL INC</div>
  <nav class="main-nav">
    <span class="active">HOME</span><span>ABOUT US</span><span>PRODUCTS</span><span>PROJECT GALLERY</span><span>CONTACT US</span><span>GET A QUOTE</span>
  </nav>
</header>

<main class="content">
  <div class="slider-image" role="img" aria-label="Photo of a modern office interior with dark wood walls, red accents and a dining table by city windows"></div>
  <div class="slider-tabs">
    <div class="tab"><h3>SAMPLE TITLE</h3>Lorem ipsum dolor sit amet,<br>consectetuer elit<br>Slider with Horizontal Tabs</div>
    <div class="tab"><h3>SAMPLE TITLE</h3>Lorem ipsum dolor sit amet,<br>consectetuer elit<br>Slider with Horizontal Tabs</div>
    <div class="tab"><h3>SAMPLE TITLE</h3>Lorem ipsum dolor sit amet,<br>consectetuer elit<br>Slider with Horizontal Tabs</div>
    <div class="tab"><h3>SAMPLE TITLE</h3>Lorem ipsum dolor sit amet,<br>consectetuer elit<br>Slider with Horizontal Tabs</div>
  </div>
</main>

<footer class="site-footer">
  <div class="col" style="left:134px">
    <h2>Our Services</h2>
    <div class="service"><div class="thumb" role="img" aria-label="Post frame building under construction"></div><p>Complete post frame<br>building packages</p></div>
    <div class="service"><div class="thumb" role="img" aria-label="Residential metal roof panels" style="background:linear-gradient(160deg,#ddd,#556)"></div><p>Residential metal<br>roofing</p></div>
    <div class="service" style="margin-top:12px"><div class="thumb" role="img" aria-label="Agricultural metal building" style="background:linear-gradient(170deg,#c9b79a,#7a3a2a)"></div><p>Commercial and<br>agricultural<br>applications</p></div>
  </div>
  <div class="col" style="left:379px">
    <h2>Quick Links</h2>
    <ul class="links"><li>Home</li><li>About Us</li><li>Products</li><li>Project Gallery</li><li>Contact Us</li><li>Get a Quote</li></ul>
  </div>
  <div class="col hours" style="left:625px">
    <h2>Working Hours</h2>
    <p><b>Better yet, see us in person!</b></p>
    <p>We love our customers, so feel free to visit during normal business hours.</p>
    <p><b>Hours</b></p>
    <p>Monday - Friday: 7am - 5pm</p>
    <p>Saturday: 7AM - 12PM</p>
    <p>Sunday: Closed</p>
  </div>
  <div class="col contact" style="left:871px">
    <h2>Contact Us</h2>
    <p>PELBROOK METAL INC PHONE :<br>555-014-0765 FAX : 555-014-4931</p>
  </div>
</footer>

<div class="copyright">Copyright © 2016 PELBROOK METAL INC - All Rights Reserved.</div>
</body>
</html>
```